Psychology practice - information brochure/flyer - half A4 page folded (4 sides)

We need a brochure/flyer to market our psychology service to GPs (Doctors). We need to demonstrate to the doctors that we are the right choice for their patients, and that we cover a large range of services so all of their patients needs are met. We will demonstrate this by listing our range of services and our team of psychologists. We have two locations in Sydney and offer high end services. I've attached our company logo but we remain flexible regarding the style of the brochures. I will provide more details (services, locations & psychologist credentials) once our preferred brochure design has been selected.

```html
<!DOCTYPE html>
<html lang="en">
<head>
<meta charset="utf-8">
<title>Psychology Practice Brochure</title>
<link href="https://fonts.googleapis.com/css2?family=Open+Sans:wght@400;600;700&family=Arimo:wght@700&display=swap" rel="stylesheet">
<style>
  :root{
    --page-bg:#e9e6e1;
    --paper:#ffffff;
    --grass-dark:#2f5e22;
    --grass-mid:#4d8a33;
    --grass-light:#6aa044;
    --accent:#f7b90f;
    --label-bg:#4e4e4e;
    --ink:#2b2b2b;
    --fee-head:#8a3b0c;
    --footer:#3f3f3f;
    --photo-soft:#dfe4e8;
  }
  *{margin:0;padding:0;box-sizing:border-box}
  html,body{width:1200px;height:878px;overflow:hidden;background:var(--page-bg)}
  body{font-family:"Open Sans",Arial,sans-serif;color:var(--ink)}
  .brochure{position:absolute;left:0;top:15px;width:1200px;height:848px;background:var(--paper);overflow:hidden;box-shadow:0 2px 8px rgba(0,0,0,.25)}
  .waves{position:absolute;left:0;top:0}
  .fold{position:absolute;left:598px;top:0;width:6px;height:848px;background:linear-gradient(90deg,rgba(0,0,0,.05),rgba(0,0,0,0))}
  .headline{position:absolute;right:50px;top:52px;text-align:right;color:#fff;font-weight:700;font-size:30px;line-height:41px;letter-spacing:.2px}
  .headline .soft{color:#dfead0;font-weight:600}
  .photo{position:absolute}
  .photo-elder{left:189px;top:412px;width:200px;height:146px;background:radial-gradient(ellipse at 65% 50%,#cfe3e6 0%,#e8eef0 55%,rgba(255,255,255,0) 75%)}
  .photo-group{left:282px;top:672px;width:316px;height:176px;background:radial-gradient(ellipse at 60% 70%,#c9d4dd 0%,#e4e8ec 55%,rgba(255,255,255,0) 85%)}
  .photo-session{left:809px;top:297px;width:391px;height:295px;background:radial-gradient(ellipse at 60% 55%,#d9d4cf 0%,#e8e9eb 50%,rgba(255,255,255,0) 78%)}
  .label{position:absolute;height:29px;background:var(--label-bg);clip-path:polygon(0 0,88% 0,100% 100%,0 100%);color:var(--accent);font-family:"Arimo",Arial,sans-serif;font-weight:700;font-size:15.5px;line-height:29px;padding-left:9px}
  .list{position:absolute;list-style:none;font-size:12.6px;line-height:20.65px}
  .list li{position:relative;padding-left:22px}
  .list li::before{content:"";position:absolute;left:0;top:9px;width:5px;height:5px;border-radius:50%;background:var(--accent)}
  .services{left:60px;top:349px}
  .clients{left:405px;top:350px}
  .hours{position:absolute;left:398px;top:598px;font-size:12.6px;line-height:22px}
  .hours b{font-weight:700}
  .clinicians{position:absolute;left:646px;top:351px;list-style:none}
  .clinician{position:relative;padding-left:14px;margin-bottom:13px}
  .clinician svg{position:absolute;left:0;top:1px}
  .clinician h3{font-size:12px;font-weight:700;line-height:16px}
  .clinician p{font-size:8.4px;line-height:12px;color:#333}
  .clinician .lang{color:#c0261b}
  .fees{position:absolute;left:650px;top:605px;font-size:10.8px}
  .fees h4{color:var(--fee-head);font-weight:700;font-size:10.8px;margin-bottom:8px}
  .fees ul{list-style:none;margin-bottom:13px}
  .fees li{position:relative;padding-left:16px;line-height:18px;font-weight:600}
  .fees li::before{content:"";position:absolute;left:2px;top:7px;width:5px;height:5px;background:var(--accent);transform:rotate(45deg)}
  .fees .gap{margin-top:4px}
  .web{position:absolute;left:890px;top:817px;color:#fff;font-size:12.8px;letter-spacing:.3px;display:flex;align-items:center;gap:8px}
</style>
</head>
<body>
<main class="brochure">
  <svg class="waves" width="1200" height="848" viewBox="0 0 1200 848" aria-hidden="true">
    <defs>
      <linearGradient id="grass" x1="0" y1="0" x2="1" y2="1">
        <stop offset="0" stop-color="#5f9a3d"/>
        <stop offset=".5" stop-color="#4a8230"/>
        <stop offset="1" stop-color="#3a6d27"/>
      </linearGradient>
    </defs>
    <path d="M0,0 H1200 V303 C1100,262 950,212 800,238 C700,255 620,272 480,266 C300,260 120,214 0,140 Z" fill="#f7b90f"/>
    <path d="M0,0 H1200 V290 C1100,250 950,200 800,225 C700,240 620,258 480,254 C300,250 120,200 0,125 Z" fill="url(#grass)"/>
    <path d="M598,848 C740,845 880,780 1040,770 C1110,766 1170,780 1200,790 V848 Z" fill="#f7b90f"/>
    <path d="M640,848 C770,846 900,792 1050,782 C1115,778 1170,790 1200,798 V848 Z" fill="#3f3f3f"/>
  </svg>
  <div class="photo" role="img" aria-label="Smiling young man lying on the grass with hands behind his head" style="left:220px;top:20px;width:320px;height:235px;background:radial-gradient(ellipse at 50% 50%,rgba(240,235,215,.35),rgba(255,255,255,0) 70%)"></div>
  <div class="fold"></div>

  <h1 class="headline">WE’RE HERE TO HELP<br>YOU GET THE <span class="soft">POSITIVE CHANGE</span><br>YOU’RE LOOKING FOR</h1>

  <div class="photo photo-elder" role="img" aria-label="Elderly woman holding hands with a carer"></div>
  <div class="photo photo-group" role="img" aria-label="Therapist talking with a couple on a sofa"></div>
  <div class="photo photo-session" role="img" aria-label="Psychologist in session with a female client"></div>

  <h2 class="label" style="left:47px;top:306px;width:244px">Type of Services we provide:</h2>
  <ul class="list services">
    <li>Anxiety</li><li>Depression</li><li>Phobias</li><li>Intellectual disability</li><li>Learning difficulties</li><li>Bullying</li><li>Study stress</li><li>Procrastination</li><li>WorkCover</li><li>Stress management</li><li>Rehabilitation psychology</li><li>Addiction and relapse prevention</li><li>Attention Deficit Hyperactivity Disorder (ADHD)</li><li>Anger management</li><li>Divorce/separation</li><li>Pregnancy</li><li>Post-Traumatic Stress Disorder (PTSD)</li><li>Couples/Family Therapy</li><li>Domestic Violence</li><li>Non-Suicidal Self-Harm</li><li>Grief and loss</li><li>Eating disorders/body image</li><li>Trauma</li>
  </ul>

  <h2 class="label" style="left:382px;top:305px;width:198px;padding-left:20px">Our Client Groups:</h2>
  <ul class="list clients">
    <li>Children 5-12</li><li>Adolescents</li><li>Adults</li><li>Veterans</li><li>Victims of crime</li><li>Injured workers</li><li>Culturally and Linguistically<br>Diverse backgrounds</li><li>Refugees</li>
  </ul>

  <h2 class="label" style="left:382px;top:555px;width:198px;padding-left:20px">Hours of Operation</h2>
  <div class="hours">
    <p><b>Monday – Friday :</b>&nbsp;&nbsp;&nbsp;8am-6pm</p>
    <p><b>&nbsp;Saturday :</b>&nbsp;&nbsp;&nbsp;9am – 1pm</p>
  </div>

  <h2 class="label" style="left:638px;top:306px;width:174px">Our Clinicians</h2>
  <ul class="clinicians">
    <li class="clinician">
      <svg width="9" height="14" viewBox="0 0 9 14"><path d="M2,14 C1,9 3,4 7,0 C5,5 5,9 6,14 Z" fill="var(--accent)"/></svg>
      <h3>Dr Helena Marris</h3>
      <p>DClinPsych, MA, BSc(Psych),<br>BPsych (Hons),<span class="lang">fluent in Greek</span></p>
    </li>
    <li class="clinician">
      <svg width="9" height="14" viewBox="0 0 9 14"><path d="M2,14 C1,9 3,4 7,0 C5,5 5,9 6,14 Z" fill="var(--accent)"/></svg>
      <h3>Dr Thomas Edward Hale</h3>
      <p>DPhil (Psych), BA-Psych (Hons),<br>GradDipEd, GDipMgt, MAPS, FCOP</p>
    </li>
    <li class="clinician">
      <svg width="9" height="14" viewBox="0 0 9 14"><path d="M2,14 C1,9 3,4 7,0 C5,5 5,9 6,14 Z" fill="var(--accent)"/></svg>
      <h3>Laura Bennett</h3>
      <p>MPsych (Clin), BPsych (Hons)</p>
    </li>
  </ul>

  <h2 class="label" style="left:639px;top:558px;width:174px">Our Fee Structure</h2>
  <section class="fees">
    <h4>BusinessHours – 9am to 5pm</h4>
    <ul>
      <li><b>$150</b> per session for General Psychologist, with Medicare Rebate of <b>$84.80</b></li>
      <li><b>$190</b> per session for Clinical Psychologist, with Medicare Rebate of <b>$124.50</b></li>
    </ul>
    <h4 class="gap">Out of Hours – weekends and after 5pm</h4>
    <ul>
      <li><b>$170</b> per session for General Psychologist, with Medicare Rebate of <b>$84.80</b></li>
      <li><b>$210</b> per session for Clinical Psychologist, with Medicare Rebate of <b>$124.50</b></li>
    </ul>
  </section>

  <p class="web">
    <svg width="15" height="15" viewBox="0 0 16 16" aria-hidden="true"><g fill="none" stroke="#fff" stroke-width="1.3"><circle cx="8" cy="8" r="6.5"/><ellipse cx="8" cy="8" rx="3" ry="6.5"/><path d="M1.5,8 H14.5 M2.5,4.5 H13.5 M2.5,11.5 H13.5"/></g></svg>
    www.clearpathpsychology.com.au
  </p>
</main>
</body>
</html>
```